INNOVATIVE DESIGN NEEDED FOR FINANCIAL COMPANY

INTERNATIONAL FIRM IN HONG KONG NEEDS A MODERN BUSINESS CARD DESIGN. ONE SIDE ENGLISH OTHER SIDE IN CHINESE. WE ARE OPEN TO CHANGING FONTS AND COLOR. SHOULD BE A CARD THAT IS PROFESSIONAL DEALING WITH HIGH NET WORTH CLIENTELE. BOTH SIDES OF THE CARD WILL BE THE SAME, HOWEVER, THE WORDING ON ONE SIDE WILL BE ENGLISH AND THE OTHER SIDE IN CHINESE (CAN ASSIST IN THE LETTERING - CAN PROVIDE ONCE CARD DESIGN IS ACCEPTED.

Target Market(s)

Hong Kong/CHINA

Contact Information for Business Card

ATTRACTIVE MODERN

```html
<!DOCTYPE html>
<html lang="en">
<head>
<meta charset="utf-8">
<title>Larchwood Capital Partners – Business Cards</title>
<link href="https://fonts.googleapis.com/css2?family=Roboto:wght@400;500;700&family=Noto+Sans+TC:wght@400;700&display=swap" rel="stylesheet">
<style>
  :root {
    --page-bg: #e4e4e4;
    --card-top: #22a07c;
    --card-bottom: #148a65;
    --ink: #ffffff;
    --mark-area: #ffffff;
  }
  html, body {
    margin: 0;
    padding: 0;
    width: 1200px;
    height: 1200px;
    overflow: hidden;
    background: var(--page-bg);
    font-family: "Roboto", "Noto Sans TC", sans-serif;
  }
  .canvas {
    position: relative;
    width: 1200px;
    height: 1200px;
  }
  .card {
    position: absolute;
    left: 262px;
    width: 800px;
    height: 457px;
    transform: scale(0.8575);
    transform-origin: top left;
    background: linear-gradient(180deg, var(--card-top), var(--card-bottom));
    color: var(--ink);
    overflow: hidden;
  }
  .card--english { top: 165px; }
  .card--chinese { top: 653px; }

  .brand {
    position: absolute;
    left: 45px;
    top: 56px;
    display: flex;
    align-items: center;
    gap: 12px;
  }
  .brand__dot {
    width: 56px;
    height: 56px;
    border-radius: 50%;
    background: var(--ink);
    flex: none;
  }
  .brand__name {
    font-family: "Roboto", "Noto Sans TC", sans-serif;
    font-weight: 700;
    line-height: 1.1;
  }
  .brand__name-zh { font-size: 22px; letter-spacing: 1px; display: block; }
  .brand__name-en { font-size: 12px; letter-spacing: 1.2px; display: block; }

  .mark-area {
    position: absolute;
    left: 412px;
    top: 40px;
    width: 368px;
    height: 417px;
    background: var(--mark-area);
    opacity: 0.12;
    border-radius: 170px 170px 0 0;
  }

  .person {
    position: absolute;
    left: 44px;
    top: 160px;
  }
  .person__name { font-size: 30px; font-weight: 500; margin: 0; line-height: 1.1; }
  .person__title { font-size: 20px; font-weight: 500; margin: 2px 0 0; }
  .card--chinese .person { top: 136px; }
  .card--chinese .person__name { font-weight: 400; font-size: 31px; }
  .card--chinese .person__title { font-weight: 400; margin-top: 10px; }

  .address {
    position: absolute;
    left: 46px;
    top: 232px;
    font-size: 19px;
    line-height: 25px;
    margin: 0;
    font-style: normal;
  }

  .contacts {
    position: absolute;
    left: 46px;
    top: 293px;
    list-style: none;
    margin: 0;
    padding: 0;
    font-size: 19px;
  }
  .contacts li {
    display: flex;
    align-items: center;
    height: 25.6px;
  }
  .contacts svg {
    width: 18px;
    height: 18px;
    margin-right: 13px;
    fill: var(--ink);
    flex: none;
  }
</style>
</head>
<body>
<div class="canvas">

  <!-- English side -->
  <section class="card card--english">
    <div class="brand">
      <span class="brand__dot"></span>
      <span class="brand__name">
        <span class="brand__name-zh">樺林資本管理有限公司</span>
        <span class="brand__name-en">Larchwood Capital Partners Ltd</span>
      </span>
    </div>
    <div class="mark-area" role="img" aria-label="Large brand symbol area"></div>

    <div class="person">
      <h1 class="person__name">Daniel Hart</h1>
      <p class="person__title">President</p>
    </div>
    <address class="address">2140 Maple Ridge Road<br>Juneau, Alaska 99801</address>

    <ul class="contacts">
      <li><svg viewBox="0 0 24 24"><path d="M6.6 10.8a15.2 15.2 0 0 0 6.6 6.6l2.2-2.2c.3-.3.7-.4 1-.2 1.1.4 2.3.6 3.6.6.6 0 1 .4 1 1V20c0 .6-.4 1-1 1A17 17 0 0 1 3 4c0-.6.4-1 1-1h3.5c.6 0 1 .4 1 1 0 1.3.2 2.5.6 3.6.1.3 0 .7-.2 1z"/></svg>555-214-7730</li>
      <li><svg viewBox="0 0 24 24"><path d="M7 1h10a2 2 0 0 1 2 2v18a2 2 0 0 1-2 2H7a2 2 0 0 1-2-2V3a2 2 0 0 1 2-2zm0 3v15h10V4z"/></svg>555-418-2291</li>
      <li><svg viewBox="0 0 24 24"><path d="M6 2h9l3 3v5H6zM3 11h18v7H3zm2 9h14v2H5z"/></svg>555-362-0846</li>
      <li><svg viewBox="0 0 24 24"><path d="M2 6h20v12H2zm2 2v.5l8 5 8-5V8l-8 5z"/></svg>info@larchwoodcap.com</li>
      <li><svg viewBox="0 0 24 24"><circle cx="12" cy="12" r="10"/></svg>www.larchwoodcap.com</li>
    </ul>
  </section>

  <!-- Chinese side -->
  <section class="card card--chinese" lang="zh-Hant">
    <div class="brand">
      <span class="brand__dot"></span>
      <span class="brand__name">
        <span class="brand__name-zh">樺林資本管理有限公司</span>
        <span class="brand__name-en">Larchwood Capital Partners Ltd</span>
      </span>
    </div>
    <div class="mark-area" role="img" aria-label="Large brand symbol area"></div>

    <div class="person">
      <h1 class="person__name">丹尼尔哈特</h1>
      <p class="person__title">主席</p>
    </div>
    <address class="address">2140 Maple Ridge Road<br>朱諾, 阿拉斯加州99801</address>

    <ul class="contacts">
      <li><svg viewBox="0 0 24 24"><path d="M6.6 10.8a15.2 15.2 0 0 0 6.6 6.6l2.2-2.2c.3-.3.7-.4 1-.2 1.1.4 2.3.6 3.6.6.6 0 1 .4 1 1V20c0 .6-.4 1-1 1A17 17 0 0 1 3 4c0-.6.4-1 1-1h3.5c.6 0 1 .4 1 1 0 1.3.2 2.5.6 3.6.1.3 0 .7-.2 1z"/></svg>555-214-7730</li>
      <li><svg viewBox="0 0 24 24"><path d="M7 1h10a2 2 0 0 1 2 2v18a2 2 0 0 1-2 2H7a2 2 0 0 1-2-2V3a2 2 0 0 1 2-2zm0 3v15h10V4z"/></svg>555-418-2291</li>
      <li><svg viewBox="0 0 24 24"><path d="M6 2h9l3 3v5H6zM3 11h18v7H3zm2 9h14v2H5z"/></svg>555-362-0846</li>
      <li><svg viewBox="0 0 24 24"><path d="M2 6h20v12H2zm2 2v.5l8 5 8-5V8l-8 5z"/></svg>info@larchwoodcap.com</li>
      <li><svg viewBox="0 0 24 24"><circle cx="12" cy="12" r="10"/></svg>www.larchwoodcap.com</li>
    </ul>
  </section>

</div>
</body>
</html>
```